new marketing company logo and business card

design logo and biz card for marketing start up.

My company name needs a brand logo designed: Cedar Hollow Marketing Co.
Tagline: Sales - Marketing - Brand Building

Sister Bay is the name of my favorite place, in Wisconsin, but the business is NOT BASED there. It should evoke warmth, friendliness, professionalism, and marketing services from a seasoned marketer.

Target Market(s)

I am selling my services to small business that need help.

Industry/Entity Type

Marketing

Contact Information for Business Card

Cedar Hollow Marketing Co. (logo)
Sales - Marketing - Brand Building (tagline)

Maren T. Holloway
MarenTHolloway@quillpost.net
555-014-3926 mobile

Font styles to use
Serif
Sans Serif

Colors
f78f20
f37122
f68d4d
00a990
85cae6
33b8a4
faa54b

Requirements
Must have
• a logo
• a business card
Nice to have
• I'd love to see a small subtle reference to Sister Bay built in. Sister bay is named that because there are two islands called ‘sister islands’ that flank the bay. If you google this you will see.
• I like warm, earthy colors. But, I am a fun, approachable, real person. Not stand-offish. Should be warm and appealing yet professional.
Should not have
• nothing cartoon-ish. no child-like fonts. this is a professional business.

```html
<!DOCTYPE html>
<html lang="en">
<head>
<meta charset="UTF-8">
<title>Cedar Hollow Marketing Co. — Business Card</title>
<link rel="stylesheet" href="https://fonts.googleapis.com/css2?family=Montserrat:wght@500;600&family=Open+Sans:ital,wght@0,400;1,700&display=swap">
<style>
  :root {
    --backdrop: #e4e5e4;
    --card-white: #ffffff;
    --brand-orange: #f37122;
    --ink: #1a1a1a;
    --pattern-light: #f7f7f7;
    --pattern-mid: #ececec;
  }
  * { margin: 0; padding: 0; box-sizing: border-box; }
  html, body {
    width: 1200px;
    height: 809px;
    overflow: hidden;
    background: var(--backdrop);
  }
  .business-card {
    position: absolute;
    left: 100px;
    top: 118px;
    width: 1000px;
    height: 572px;
    background: var(--card-white);
    box-shadow: 0 6px 18px rgba(0,0,0,0.12);
    overflow: hidden;
  }
  .texture-field {
    position: absolute;
    left: 300px;
    top: 40px;
    width: 700px;
    height: 300px;
    background: radial-gradient(ellipse at 65% 55%, var(--pattern-mid) 0%, var(--pattern-light) 45%, rgba(255,255,255,0) 75%);
  }
  .holder-name {
    position: absolute;
    left: 70px;
    top: 70px;
    font-family: "Open Sans", sans-serif;
    font-style: italic;
    font-weight: 700;
    font-size: 30px;
    color: var(--ink);
  }
  .company-name {
    position: absolute;
    left: 70px;
    top: 182px;
    font-family: "Montserrat", sans-serif;
    font-weight: 600;
    font-size: 42px;
    letter-spacing: 1px;
    text-transform: uppercase;
    color: var(--brand-orange);
  }
  .tagline {
    position: absolute;
    left: 70px;
    top: 236px;
    font-family: "Montserrat", sans-serif;
    font-weight: 500;
    font-size: 24px;
    letter-spacing: 1.5px;
    text-transform: uppercase;
    color: var(--ink);
  }
  .contact-band {
    position: absolute;
    left: 0;
    bottom: 0;
    width: 100%;
    height: 232px;
    background: var(--brand-orange);
  }
  .contact-item {
    position: absolute;
    display: flex;
    align-items: center;
    gap: 18px;
    font-family: "Open Sans", sans-serif;
    font-size: 25px;
    letter-spacing: 0.5px;
    color: var(--card-white);
  }
  .contact-phone { left: 56px; top: 34px; }
  .contact-email { right: 60px; bottom: 40px; }
  .contact-icon { width: 22px; height: 22px; fill: var(--card-white); }
</style>
</head>
<body>
  <div class="business-card">
    <div class="texture-field" role="img" aria-label="Faint grey mosaic of small squares fading across the card"></div>
    <p class="holder-name">Maren T. Holloway</p>
    <h1 class="company-name">Cedar Hollow Marketing Co</h1>
    <p class="tagline">Sales - Marketing - Brand Building</p>
    <div class="contact-band">
      <div class="contact-item contact-phone">
        <svg class="contact-icon" viewBox="0 0 24 24" aria-hidden="true">
          <path d="M6.6 10.8a15.1 15.1 0 0 0 6.6 6.6l2.2-2.2a1 1 0 0 1 1-.25 11.4 11.4 0 0 0 3.6.57 1 1 0 0 1 1 1V20a1 1 0 0 1-1 1A17 17 0 0 1 3 4a1 1 0 0 1 1-1h3.5a1 1 0 0 1 1 1c0 1.25.2 2.45.57 3.57a1 1 0 0 1-.25 1z"/>
        </svg>
        <span>555-014-3926</span>
      </div>
      <div class="contact-item contact-email">
        <svg class="contact-icon" viewBox="0 0 24 24" aria-hidden="true">
          <path d="M2 5h20v14H2z M2 5l10 8 10-8" fill="var(--card-white)" stroke="var(--brand-orange)" stroke-width="1.6" stroke-linejoin="round"/>
        </svg>
        <span>marentholloway@quillpost.net</span>
      </div>
    </div>
  </div>
</body>
</html>
```